stichtingveln . Eu

With its head office in Amsterdam stichtingveln.eu we will have offices in the Netherlands, Luxembourg , Belgium, switzerland, Monaco, Liechtenstein and we want pictures of those countries .
VELN.CA a popular Canadian non profit is opening in the Europe and will require a website that appeals those countries we specified.
Please focus on reuse of electronics. Mention ‘WEEE’
Donations to charities, non profit, school and orphanage.
Donates to 3rd world countries like Madagascar
Industry
Technology
Color Preferences
green and blue and similar to veln.ca
Our Ideas & Additional Information
veln.ca logo
use these websites as examples to copy and make similar websites
www.qrb.mg
www.veln.ca
www.racunalnodom.ba
stichtingveln.eu - non profit , foundation , association
Target Market(s)
Amsterdam
Industry/Entity Type
Technology, nonprofit
Number of Pages Required
1 page

```html
<!DOCTYPE html>
<html lang="mg">
<head>
<meta charset="utf-8">
<title>QRB – Fanindroany Ny Elektrônikao</title>
<link href="https://fonts.googleapis.com/css2?family=Poppins:wght@400;500;600;700&display=swap" rel="stylesheet">
<style>
:root{
  --green:#62b35b;
  --green-dark:#3f8f3a;
  --blue:#1c58b0;
  --blue-deep:#123f8a;
  --mint:#eef4ea;
  --ink:#1d1d1f;
  --muted:#5d5d63;
  --line:#dfe3e0;
  --white:#ffffff;
  --footer:#141416;
}
*{box-sizing:border-box;margin:0;padding:0}
html,body{width:1200px;height:5149px;overflow:hidden}
body{font-family:"Poppins",sans-serif;color:var(--ink);background:var(--white);position:relative}
.abs{position:absolute}
a{text-decoration:none;color:inherit}

/* header */
.site-header{left:0;top:0;width:1200px;height:94px;background:var(--white);z-index:5}
.brand{left:100px;top:10px;display:flex;align-items:center;gap:10px}
.brand-mark{width:18px;height:18px;border-radius:50%;background:var(--green)}
.brand-name{font-weight:700;font-size:22px;color:var(--green-dark)}
.main-nav{left:290px;top:34px;display:flex;gap:28px;font-size:13px;font-weight:500}
.nav-cta{left:910px;top:25px;width:184px;height:42px;border-radius:21px;background:var(--green);color:var(--white);font-size:12px;font-weight:600;display:flex;align-items:center;justify-content:center}

/* hero */
.hero-photo{left:0;top:94px;width:1200px;height:620px;background:linear-gradient(110deg,#6b4a2e 0%,#8c6a47 35%,#3a3f7a 65%,#2a3d95 100%)}
.hero-wave{left:0;top:560px;width:1200px;height:160px}
.hero-copy{left:105px;top:172px;width:460px;color:var(--white)}
.hero-copy h1{font-size:35px;line-height:50px;font-weight:700}
.hero-copy p{font-size:13px;line-height:20px;margin-top:26px}
.btn{display:inline-flex;align-items:center;justify-content:center;border-radius:22px;font-size:12px;font-weight:600;color:var(--white)}
.hero-actions{left:105px;top:449px;display:flex;gap:16px}
.btn-green{background:var(--green);height:42px;padding:0 25px}
.btn-blue{background:var(--blue);height:42px;padding:0 28px}
.hero-badges{left:105px;top:518px;display:flex;gap:8px}
.badge{width:84px;height:84px;border-radius:50%;background:var(--white);border:6px solid var(--green)}
.scroll-dot{left:554px;top:664px;width:88px;height:88px;border-radius:50%;background:var(--white);display:flex;align-items:center;justify-content:center;box-shadow:0 6px 16px rgba(0,0,0,.06)}

/* about */
.about-visual{left:150px;top:780px;width:440px;height:420px}
.about-copy{left:657px;top:810px;width:400px}
.about-copy h2{font-size:31px;line-height:38px;font-weight:600}
.about-copy p{font-size:12.5px;line-height:23px;color:var(--muted);margin-top:18px}
.deco-ring{width:112px;height:112px;border-radius:50%;border:2px dashed var(--blue)}
.deco-disc{width:84px;height:84px;border-radius:50%;background:var(--blue)}

/* bands */
.band{left:0;width:1200px}
.card{background:var(--white);border-radius:6px;box-shadow:0 6px 24px rgba(30,60,30,.07)}
.feature{top:1475px;width:285px;height:300px;text-align:center;padding:34px 24px 0}
.feature-icon{width:84px;height:84px;margin:0 auto;border-radius:50%;border:2px dashed var(--green);display:flex;align-items:center;justify-content:center}
.feature-icon span{width:64px;height:64px;border-radius:50%;background:var(--green);display:flex;align-items:center;justify-content:center}
.feature h3{font-size:13.5px;font-weight:600;margin-top:30px}
.feature p{font-size:12px;line-height:21px;color:var(--muted);margin-top:12px}

/* partnership */
.partner-copy{left:140px;top:2010px;width:400px}
.partner-copy h2{font-size:31px;font-weight:600}
.partner-copy p{font-size:12.5px;line-height:23px;color:var(--muted);margin-top:18px}
.btn-outline{left:140px;top:2270px;height:42px;width:210px;border-radius:21px;background:var(--blue);color:var(--white);font-size:12px;font-weight:600;display:flex;align-items:center;justify-content:space-between;padding:0 4px 0 28px}
.arrow-dot{width:34px;height:34px;border-radius:50%;background:var(--white);display:flex;align-items:center;justify-content:center}
.partner-art{left:635px;top:1960px;width:425px;height:410px}

/* offices */
.section-title{left:0;width:1200px;text-align:center;font-size:31px;font-weight:600}
.office{width:285px;height:300px;padding:10px 10px 0}
.office-photo{width:265px;height:170px;border-radius:4px}
.office h3{font-size:16px;font-weight:600;margin:22px 0 0 8px}
.office p{font-size:12px;line-height:21px;color:var(--muted);margin:8px 0 0 8px;width:240px}

/* stats */
.stat{width:300px;height:300px;border-radius:50%;display:flex;flex-direction:column;align-items:center;justify-content:center;text-align:center}
.stat-ring{border:2px dashed var(--blue)}
.stat-fill{background:var(--green);color:var(--white)}
.stat strong{font-size:37px;font-weight:600;color:var(--blue)}
.stat-fill strong{color:var(--white)}
.stat span{font-size:17px;line-height:24px;margin-top:8px;color:#444}
.stat-fill span{color:var(--white)}

/* cta band */
.cta-col{top:4080px;width:460px;color:var(--white)}
.cta-col h2{font-size:32px;font-weight:500}
.cta-col p{font-size:12px;line-height:22px;margin-top:12px}
.btn-pill-green{margin-top:26px;height:42px;width:158px;border-radius:21px;background:var(--green);border:2px solid var(--white);color:var(--white);font-size:12px;font-weight:600;display:flex;align-items:center;justify-content:space-between;padding:0 4px 0 20px}

/* contact */
.contact-copy{left:140px;top:4525px;width:440px}
.contact-copy h2{font-size:31px;font-weight:600}
.contact-copy>p{font-size:12px;line-height:22px;color:var(--muted);margin-top:16px}
.contact-item{display:flex;gap:22px;align-items:flex-start;margin-top:34px}
.contact-icon{width:76px;height:76px;border-radius:50%;border:2px dashed var(--green);display:flex;align-items:center;justify-content:center;flex:none}
.contact-icon span{width:60px;height:60px;border-radius:50%;background:var(--green);display:flex;align-items:center;justify-content:center}
.contact-item h3{font-size:17px;font-weight:600;margin-top:4px}
.contact-item p{font-size:12px;line-height:21px;color:var(--muted);margin-top:4px}
.form-card{left:607px;top:4485px;width:450px;height:545px;border-top:4px solid var(--green);padding:34px 30px}
.form-card h2{font-size:29px;font-weight:600}
.field{margin-top:30px;border-bottom:1px solid var(--line);padding-bottom:10px;position:relative}
.field label{display:block;font-size:12px;color:#333}
.field .value{font-size:12px;color:#9a9ea3;margin-top:10px}
.field svg{position:absolute;right:2px;bottom:12px}
.field-tall{height:88px}
.submit{margin-top:52px;height:42px;width:142px;border-radius:21px;background:var(--blue);color:var(--white);font-size:12px;font-weight:600;display:flex;align-items:center;justify-content:space-between;padding:0 4px 0 26px}

.site-footer{left:0;top:5108px;width:1200px;height:41px;background:var(--footer);color:#e7e7e7;font-size:11px;display:flex;align-items:center;justify-content:space-between;padding:0 142px}
</style>
</head>
<body>

<header class="abs site-header">
  <a class="abs brand" href="#"><span class="brand-mark"></span><span class="brand-name">QRB</span></a>
  <nav class="abs main-nav">
    <a href="#">An-trano</a><a href="#">About</a><a href="#">Manomeza</a><a href="#">WEEE Recycling</a><a href="#">Tany</a><a href="#">Fiantraikany</a><a href="#">Contact</a>
  </nav>
  <a class="abs nav-cta" href="#">Manome Electronics</a>
</header>

<section>
  <div class="abs hero-photo" role="img" aria-label="Ankizy roa mianatra amin'ny solosaina ao an-dakilasy"></div>
  <svg class="abs hero-wave" viewBox="0 0 1200 160" preserveAspectRatio="none" aria-hidden="true">
    <path d="M0 40 C220 150 480 170 720 110 C900 65 1060 40 1200 60 L1200 160 L0 160Z" fill="#fff"/>
    <path d="M0 40 C220 150 480 170 720 110 C900 65 1060 40 1200 60 L1200 78 C1060 60 900 85 720 128 C480 180 220 165 0 62Z" fill="var(--blue)"/>
  </svg>
  <div class="abs hero-copy">
    <h1>Omeo Fiainana Fanindroany Ny Elektrônikao – Manomeza Anio!</h1>
    <p>Manohana Sekoly, Asa Fanasoavana &amp; Vondrom piarahamonina Manerana an'i Eoropa &amp; Ambony</p>
  </div>
  <div class="abs hero-actions">
    <a class="btn btn-green" href="#">Manome izao</a>
    <a class="btn btn-blue" href="#">Mianara Momba Ny WEEE</a>
  </div>
  <div class="abs hero-badges"><span class="badge"></span><span class="badge"></span></div>
  <div class="abs scroll-dot">
    <svg width="30" height="40" viewBox="0 0 30 40" aria-hidden="true"><rect x="6" y="4" width="18" height="30" rx="9" fill="none" stroke="var(--green)" stroke-width="2"/><path d="M11 18l4 4 4-4" fill="none" stroke="var(--green)" stroke-width="2"/></svg>
  </div>
</section>

<section>
  <svg class="abs about-visual" viewBox="0 0 440 420" aria-hidden="true">
    <path d="M220 30 A190 190 0 1 1 60 110" fill="none" stroke="#d6ebd2" stroke-width="48"/>
    <path d="M150 12 L210 -10 L212 74Z" fill="#d6ebd2" transform="translate(20 30)"/>
  </svg>
  <div class="abs" role="img" aria-label="Mpiasa roa manamboatra solosaina ao amin'ny atrikasa" style="left:150px;top:838px;width:370px;height:345px;border-radius:50%;background:linear-gradient(135deg,#cfd4d8,#7b6f68 55%,#2c3340)"></div>
  <div class="abs about-copy">
    <h2>Omeo Fahafahana Vaovao Amin'ny Fomba Azo Antoka Indrindra</h2>
    <p>Ny fiheverana ny fampiasana ny solosaina manokana ho toy ny haitraitra dia zavatra taloha. Na dia ny asa fototra aza izao dia mitaky ny fampiasana solosaina; ny fangatahana asa, ny famitana ny asa any an-tsekoly, ny fifandraisana amin'ny fianakaviana na ny zavatra hevitra hafa toy ny fitadiavana lalana fiara fitateram-bahoaka dia sarotra raha tsy misy solosaina.</p>
    <p>Ny fikambanana "Veln Reuse Alliance" dia namolavola hetsika fanomezana solosaina ho an'ny asa soa mba hamahana izany olana izany. Ny manana fitaovana elektrônika dia namolavola hetsika fanomezana solosaina ho an'ny asa soa mba hamahana izany olana izany.</p>
  </div>
  <div class="abs deco-ring" style="left:1095px;top:1250px"></div>
  <div class="abs deco-disc" style="left:1160px;top:1330px"></div>
</section>

<section>
  <svg class="abs band" style="top:1380px;height:520px" viewBox="0 0 1200 520" preserveAspectRatio="none" aria-hidden="true">
    <path d="M0 20 C250 -10 420 40 700 30 C900 22 1050 -5 1200 10 L1200 490 C1000 520 800 430 560 460 C300 495 150 470 0 420Z" fill="var(--mint)"/>
  </svg>
  <article class="abs card feature" style="left:140px">
    <div class="feature-icon"><span><svg width="30" height="30" viewBox="0 0 30 30"><circle cx="15" cy="15" r="11" fill="none" stroke="#fff" stroke-width="2"/><path d="M15 8v7l5 3" fill="none" stroke="#fff" stroke-width="2"/></svg></span></div>
    <h3>Ahoana No Hataontsika?</h3>
    <p>Raha manana fitaovana elektronika tsy ampiasainao intsony ianao dia maka toerana sy manangona vovoka. Afaka manome fahafahana vaovao ny...</p>
  </article>
  <article class="abs card feature" style="left:456px">
    <div class="feature-icon"><span><svg width="30" height="30" viewBox="0 0 30 30"><circle cx="15" cy="14" r="11" fill="none" stroke="#fff" stroke-width="2"/><path d="M11 11a4 4 0 1 1 4 4v3M15 21v1" fill="none" stroke="#fff" stroke-width="2"/></svg></span></div>
    <h3>Fanontaniana Apetraka Matetika</h3>
    <p>Mitadiava valiny amin'ireo fanontaniana mahaliana anao, ary raha too ka tsy hanome valiny ho anao izahay dia aza misalasala mifandray aminay.</p>
  </article>
  <article class="abs card feature" style="left:774px">
    <div class="feature-icon"><span><svg width="30" height="30" viewBox="0 0 30 30"><path d="M5 10l10-5 10 5v11l-10 5-10-5z M5 10l10 5 10-5 M15 15v11" fill="none" stroke="#fff" stroke-width="2"/></svg></span></div>
    <h3>Mamandrika Fampidinana</h3>
    <p>Tonga maimaim-poana izahay mankany amin'ny adiresinao mba haka fitaovana elektronika tsy ilainao intsony. Ampiharo amin'ny alalan'ny endrika an-tserasera.</p>
  </article>
</section>

<section>
  <div class="abs partner-copy">
    <h2>Fiaraha-Miasa</h2>
    <p>Miara-miasa amin'ny " Veln Reuse Alliance " izahay. Ny "Veln Reuse Alliance" dia nanomboka niasa ny taona 2004 tao amin'ny faritanin'ny Kanada, ny nibanjinan'izy ireo manokana dia ny fiarovana ny tontolo iainana tamin'ny fampihenana ny fako elektronika, sady nandray anjara teo anivon'ny fiaraha-monina tamin'ny alalan'ny fanomezana fitaovana elektronika namboarina ho an'ny fikambanana sy ho an'olon-tsotra.</p>
  </div>
  <a class="abs btn-outline" href="#">Mifandraisa Aminay<span class="arrow-dot"><svg width="12" height="12" viewBox="0 0 12 12"><path d="M2 10L10 2M4 2h6v6" fill="none" stroke="var(--blue)" stroke-width="1.6"/></svg></span></a>
  <div class="abs partner-art" role="img" aria-label="Sary fitaovana elektronika tranainy voahodidin'ny zana-tsipìka fanodinana maitso" style="background:radial-gradient(circle at 50% 55%,#c9c0d6 0 28%,#5f9e2c 29% 48%,transparent 49%)"></div>
  <div class="abs deco-ring" style="left:-10px;top:2350px"></div>
  <div class="abs deco-disc" style="left:-42px;top:2430px"></div>
</section>

<section>
  <svg class="abs band" style="top:2480px;height:880px" viewBox="0 0 1200 880" preserveAspectRatio="none" aria-hidden="true">
    <path d="M0 40 C260 10 480 60 760 30 C950 10 1080 20 1200 0 L1200 860 C980 880 760 820 520 850 C300 878 140 860 0 830Z" fill="var(--mint)"/>
  </svg>
  <h2 class="abs section-title" style="top:2565px">Manitatra manerana an'i Eoropa</h2>

  <article class="abs card office" style="left:140px;top:2636px"><div class="office-photo" role="img" aria-label="Lakandrano sy trano ary bisikileta any Amsterdam" style="background:linear-gradient(180deg,#c7ccd2,#7d6a5a 60%,#4a4a48)"></div><h3>Pays-Bas</h3><p>Lorem ipsum dolor sit ame consetuer adipiscing elit sed diam.</p></article>
  <article class="abs card office" style="left:456px;top:2636px"><div class="office-photo" role="img" aria-label="Lapa sy loharano any Luxembourg" style="background:linear-gradient(180deg,#cfd8e2,#8f7a63 55%,#3f5b3c)"></div><h3>Luxembourg</h3><p>Lorem ipsum dolor sit ame consetuer adipiscing elit sed diam.</p></article>
  <article class="abs card office" style="left:774px;top:2636px"><div class="office-photo" role="img" aria-label="Tilikambo sy tanàna amin'ny masoandro milentika" style="background:linear-gradient(180deg,#b9c8d8,#d8a86a 60%,#514a45)"></div><h3>Belzika</h3><p>Lorem ipsum dolor sit ame consetuer adipiscing elit sed diam.</p></article>
  <article class="abs card office" style="left:140px;top:2968px"><div class="office-photo" role="img" aria-label="Katedraly sy tanàna tranainy any Soisa" style="background:linear-gradient(180deg,#2f6fc0,#c49456 60%,#4d5d3a)"></div><h3>Soisa</h3><p>Lorem ipsum dolor sit ame consetuer adipiscing elit sed diam.</p></article>
  <article class="abs card office" style="left:456px;top:2968px"><div class="office-photo" role="img" aria-label="Tanàna amoron-dranomasina any Monaco amin'ny hariva" style="background:linear-gradient(180deg,#6d6f8a,#f0a040 55%,#5a3b2e)"></div><h3>Monaco</h3><p>Lorem ipsum dolor sit ame consetuer adipiscing elit sed diam.</p></article>
  <article class="abs card office" style="left:774px;top:2968px"><div class="office-photo" role="img" aria-label="Tanàna sy lapa eny an-tendrombohitra any Liechtenstein" style="background:linear-gradient(180deg,#b9c7d4,#7a8a5c 55%,#3f5a32)"></div><h3>Liechtenstein</h3><p>Lorem ipsum dolor sit ame consetuer adipiscing elit sed diam.</p></article>
</section>

<section>
  <div class="abs deco-ring" style="left:1095px;top:3402px"></div>
  <div class="abs deco-disc" style="left:1160px;top:3482px"></div>
  <h2 class="abs section-title" style="top:3478px">Ny Fiantraikantsika Amin'ny Nomery</h2>
  <div class="abs stat stat-ring" style="left:180px;top:3570px"><strong>50000</strong><span>Fitaovana ampiasaina<br>indray</span></div>
  <div class="abs stat stat-ring" style="left:720px;top:3570px"><strong>100</strong><span>Sekoly tohanana</span></div>
  <div class="abs stat stat-fill" style="left:450px;top:3570px"><strong>200</strong><span>Taoniny amin'ny<br>E-Vaky Recycle</span></div>
</section>

<section>
  <svg class="abs band" style="top:3920px;height:510px" viewBox="0 0 1200 510" preserveAspectRatio="none" role="img" aria-label="Ankizy ao an-dakilasy, voasarona loko manga">
    <defs><linearGradient id="ctaTone" x1="0" y1="0" x2="1" y2="1"><stop offset="0" stop-color="#1d5fbf"/><stop offset="1" stop-color="#123f8a"/></linearGradient></defs>
    <path d="M0 70 C260 20 520 80 780 40 C960 12 1100 0 1200 10 L1200 470 C1000 430 760 500 520 490 C300 480 140 440 0 450Z" fill="url(#ctaTone)"/>
  </svg>
  <div class="abs cta-col" style="left:140px">
    <h2>Manome Fitaovana</h2>
    <p>Manana solosaina finday, finday, tablette ary maro hafa izahay. Mialà any amin'ny birao ny na mandamina ny fokana.</p>
    <a class="btn-pill-green" href="#">Manome izao<span class="arrow-dot"><svg width="12" height="12" viewBox="0 0 12 12"><path d="M2 10L10 2M4 2h6v6" fill="none" stroke="var(--green)" stroke-width="1.6"/></svg></span></a>
  </div>
  <div class="abs cta-col" style="left:642px">
    <h2>Tohano ara-bola</h2>
    <p>Ny fandraisanao anjara dia manampy anay hanavao ny fitaovana sy hanohana vondron-piarahamonina maro kokoa.</p>
    <a class="btn-pill-green" href="#">Manome vola<span class="arrow-dot"><svg width="12" height="12" viewBox="0 0 12 12"><path d="M2 10L10 2M4 2h6v6" fill="none" stroke="var(--green)" stroke-width="1.6"/></svg></span></a>
  </div>
</section>

<section>
  <div class="abs deco-ring" style="left:-10px;top:4455px"></div>
  <div class="abs contact-copy">
    <h2>Antsipirian'ny Fifandraisana</h2>
    <p>Ut wisi enim ad minim v quis nostrud exerci tat ullamcorper spit lobortis nisl ut aliquip ex ea comghmodo consequat. Duis autem vel eum iriure dolor hendre vulputa.</p>
    <div class="contact-item">
      <div class="contact-icon"><span><svg width="22" height="22" viewBox="0 0 22 22"><path d="M11 2a7 7 0 0 0-7 7c0 5 7 11 7 11s7-6 7-11a7 7 0 0 0-7-7z" fill="#fff"/><circle cx="11" cy="9" r="2.5" fill="var(--green)"/></svg></span></div>
      <div><h3>TOERANA</h3><p>Ut wisi enim ad minim v qu nostrud<br>exerci tat ullamcorper spit.</p></div>
    </div>
    <div class="contact-item">
      <div class="contact-icon"><span><svg width="22" height="22" viewBox="0 0 22 22"><rect x="3" y="5" width="16" height="12" rx="1" fill="#fff"/><path d="M3 6l8 6 8-6" fill="none" stroke="var(--green)" stroke-width="1.5"/></svg></span></div>
      <div><h3>MAILAKA</h3><p>info@qrb.mg</p></div>
    </div>
    <div class="contact-item">
      <div class="contact-icon"><span><svg width="22" height="22" viewBox="0 0 22 22"><path d="M6 3l3 4-2 2c1 2 3 4 5 5l2-2 4 3-2 3C10 18 4 12 3 6z" fill="#fff"/></svg></span></div>
      <div><h3>PHONE</h3><p>038 41 552 19</p></div>
    </div>
  </div>

  <form class="abs card form-card">
    <h2>Fifandraisana Haingana</h2>
    <div class="field"><label>Anarana</label><div class="value">Rija Rakoto</div><svg width="12" height="12" viewBox="0 0 12 12"><circle cx="6" cy="4" r="2.5" fill="var(--green)"/><path d="M1 11c0-3 2-4.5 5-4.5s5 1.5 5 4.5z" fill="var(--green)"/></svg></div>
    <div class="field"><label>Mailaka</label><div class="value">info@rijarakoto.mg</div><svg width="12" height="12" viewBox="0 0 12 12"><rect x="1" y="3" width="10" height="7" fill="#9a9ea3"/></svg></div>
    <div class="field"><label>Nomeraon-telefaonina</label><div class="value">123 456 7890</div><svg width="12" height="12" viewBox="0 0 12 12"><path d="M3 1l2 3-1 1c.6 1.2 1.8 2.4 3 3l1-1 3 2-1 2C5 10 2 7 1 3z" fill="#9a9ea3"/></svg></div>
    <div class="field field-tall"><label>Ahoana no azontsika anampiana?</label><div class="value">Ampidiro ny hafatrao</div><svg style="top:30px;bottom:auto" width="12" height="12" viewBox="0 0 12 12"><path d="M1 2h10v6H5l-3 3V8H1z" fill="#9a9ea3"/></svg></div>
    <button class="submit" type="button" style="border:0;font-family:inherit">Alefa izao<span class="arrow-dot"><svg width="12" height="12" viewBox="0 0 12 12"><path d="M2 10L10 2M4 2h6v6" fill="none" stroke="var(--blue)" stroke-width="1.6"/></svg></span></button>
  </form>
</section>

<footer class="abs site-footer">
  <span>© 2025 QRB. Zo rehetra voatokana.</span>
  <span>Politika manokana &nbsp;&nbsp;|&nbsp;&nbsp; Fepetra fampiasana</span>
</footer>

</body>
</html>
```